Design for Huddle app (online tool) (#102244)

Url of the app: http://huddle.moorfinch.dk

It currently has 3 main parts:
- Front: http://tealmarsh.dk/screencast/2015-12-01_12-53-36.png
- Dashboard: http://tealmarsh.dk/screencast/2015-12-01_12-54-16.png
- Meeting page: http://tealmarsh.dk/screencast/2015-12-01_12-54-53.png

The idea of the app is to have virtual meetings with other people, to take notes/minutes online and to share what is written.

Unregistered users can see only the front.

Registered users can see front, their own dashboard and the meetings which they created or to which they were invited.

The meeting itself has two roles - minute taker an attendee. The attendee can edit only the agenda so he should have different view for the other parts of the meeting compared to the minute taker who can edit everything.

In this doc it is described what are the elements per page which we want to have
https://files.quillnest.example/doc/7vKp2RtXw9LmQa4Hs8NcYe3BdZu6JfTgPo1iWxEk/edit?usp=sharing

As you can see, there is some inconsistency between the front page and the rest of the app. We would like to make it look professional and consistent on all places.

Goal: Get new responsive design where all main parts(front page, dashboard page, meeting page and profile page) will be consistent with each other.

The design should be clean, simple and with very friendly UX.
Updates

Industry/Entity Type

Online

Number of Pages Required

3 page

Font styles to use
Sans Serif

Requirements
Must have
• - Clean and simple
• - Very friendly UX

```html
<!DOCTYPE html>
<html lang="en">
<head>
<meta charset="utf-8">
<title>Minutewell – Dashboard</title>
<link href="https://fonts.googleapis.com/css2?family=Source+Sans+3:wght@300;400;600&display=swap" rel="stylesheet">
<style>
:root{
  --bg:#2b3440;
  --card:#323d4c;
  --card-line:#c9cdd4;
  --text:#f2f3f5;
  --muted:#4a5b74;
  --faint:#3e4d62;
  --accent:#f2a93b;
  --field-line:#4a5b74;
  --field-bg:#2f3a4a;
  --foot-bg:#d8d8d8;
  --foot-text:#3a3f46;
  --foot-logo:#6a6e74;
  --foot-active:#6dbf6d;
}
*{box-sizing:border-box;margin:0;padding:0}
html,body{width:1200px;height:1064px;overflow:hidden}
body{background:var(--bg);font-family:"Source Sans 3",sans-serif;color:var(--text);position:relative}
.abs{position:absolute}
.btn-new{left:63px;top:62px;width:143px;height:30px;background:var(--accent);border-radius:3px;color:#2b3440;font-size:14px;font-weight:600;letter-spacing:.3px;display:flex;align-items:center;justify-content:center}
.brand{display:flex;align-items:center;gap:10px;font-weight:300}
.brand-dot{width:36px;height:36px;border-radius:50%;background:var(--accent);opacity:.85}
.brand-top{left:509px;top:59px;font-size:20px;color:var(--text)}
.user{left:904px;top:64px;display:flex;align-items:center;gap:10px;font-size:17px}
.help{left:1107px;top:62px;width:30px;height:30px;border:1.5px solid var(--accent);border-radius:50%;color:var(--accent);font-size:14px;display:flex;align-items:center;justify-content:center}
.user-menu{right:127px;top:93px;text-align:right;list-style:none;font-size:14px;color:var(--muted);line-height:19px;font-weight:300}
.page-title{left:0;width:1200px;top:176px;text-align:center;font-size:28px;font-weight:300;letter-spacing:.5px;color:#d5d8dd}
.search{left:64px;top:241px;width:501px;height:29px;border:1px solid var(--field-line);background:var(--field-bg);border-radius:3px;display:flex;align-items:center;justify-content:space-between;padding:0 12px;font-size:13.5px;color:var(--faint);font-weight:300}
.filters{left:635px;top:241px;width:501px;height:29px;border:1px solid var(--accent);border-radius:3px;display:flex;color:var(--accent);font-size:14.5px;font-weight:300}
.filters span{display:flex;align-items:center;justify-content:center}
.filters span+span{border-left:1px solid var(--accent)}
.meetings{left:64px;top:343px;width:1072px;list-style:none}
.meeting{height:97px;background:var(--card);border:1px solid var(--card-line);border-radius:4px;padding:21px 23px 0;margin-bottom:13.5px}
.meeting-title{font-size:17px;line-height:20px;font-weight:400}
.meeting-when{font-size:15px;line-height:18px;font-weight:400}
.meeting-when time{color:var(--faint);font-weight:300;margin-right:9px}
.meeting-people{font-size:9px;margin-top:4px;color:#e4e6ea}
.meeting-people b{font-weight:600}
.site-footer{left:0;top:957px;width:1200px;height:107px;background:var(--foot-bg);color:var(--foot-text)}
.brand-foot{left:64px;top:32px;font-size:20px;color:var(--foot-logo)}
.copyright{left:0;width:1200px;top:42px;text-align:center;font-size:16px}
.foot-nav{right:63px;top:42px;display:flex;gap:21px;font-size:16px;list-style:none}
.foot-nav .active{color:var(--foot-active)}
</style>
</head>
<body>
<header>
  <div class="abs btn-new">+NEW MEETING</div>
  <div class="abs brand brand-top"><span class="brand-dot"></span>Minutewell</div>
  <div class="abs user">
    <svg width="26" height="26" viewBox="0 0 26 26" aria-hidden="true"><circle cx="13" cy="8" r="6" fill="#e6e8eb"/><path d="M1 25c0-7 5-10 12-10s12 3 12 10z" fill="#e6e8eb"/></svg>
    <span>Dorin Kelsov</span>
    <svg width="10" height="8" viewBox="0 0 10 8" aria-hidden="true"><path d="M1 2l4 4 4-4" stroke="#e6e8eb" stroke-width="1.6" fill="none"/></svg>
  </div>
  <div class="abs help">?</div>
  <ul class="abs user-menu"><li>Dashboard</li><li>My meetings</li><li>Sign out</li></ul>
</header>
<main>
  <h1 class="abs page-title">DASHBOARD</h1>
  <div class="abs search">
    <span>Search by attendees' names, meeting title, date, location. Fx. '12.11.2015'</span>
    <svg width="20" height="20" viewBox="0 0 20 20" aria-hidden="true"><circle cx="8" cy="8" r="6" stroke="#f2a93b" stroke-width="2.2" fill="none"/><path d="M12.5 12.5l6 6" stroke="#f2a93b" stroke-width="2.6" stroke-linecap="round"/></svg>
  </div>
  <nav class="abs filters">
    <span style="width:124px">Filled meetings</span>
    <span style="width:178px">My own meetings</span>
    <span style="flex:1">Meetings which I attended</span>
  </nav>
  <ul class="abs meetings">
    <li class="meeting"><h2 class="meeting-title">DEMOTITLETEST</h2><p class="meeting-when"><time>25.11.2015 &nbsp; 14:19</time>@Kestrel Hall</p><p class="meeting-people"><b>Dorin Kelsov &lt;dorin@moorfinch.dk&gt;</b>, &nbsp;Ivo Marlek &lt;ivo@moorfinch.dk&gt;, &nbsp;&lt;lena@moorfinch.dk&gt;</p></li>
    <li class="meeting"><h2 class="meeting-title">DEMOTITLETEST</h2><p class="meeting-when"><time>25.11.2015 &nbsp; 14:19</time>@Kestrel Hall</p><p class="meeting-people"><b>Dorin Kelsov &lt;dorin@moorfinch.dk&gt;</b>, &nbsp;Ivo Marlek &lt;ivo@moorfinch.dk&gt;, &nbsp;&lt;lena@moorfinch.dk&gt;</p></li>
    <li class="meeting"><h2 class="meeting-title">DEMOTITLETEST</h2><p class="meeting-when"><time>25.11.2015 &nbsp; 14:19</time>@Kestrel Hall</p><p class="meeting-people"><b>Dorin Kelsov &lt;dorin@moorfinch.dk&gt;</b>, &nbsp;Ivo Marlek &lt;ivo@moorfinch.dk&gt;, &nbsp;&lt;lena@moorfinch.dk&gt;</p></li>
    <li class="meeting"><h2 class="meeting-title">DEMOTITLETEST</h2><p class="meeting-when"><time>25.11.2015 &nbsp; 14:19</time>@Kestrel Hall</p><p class="meeting-people"><b>Dorin Kelsov &lt;dorin@moorfinch.dk&gt;</b>, &nbsp;Ivo Marlek &lt;ivo@moorfinch.dk&gt;, &nbsp;&lt;lena@moorfinch.dk&gt;</p></li>
    <li class="meeting"><h2 class="meeting-title">DEMOTITLETEST</h2><p class="meeting-when"><time>25.11.2015 &nbsp; 14:19</time>@Kestrel Hall</p><p class="meeting-people"><b>Dorin Kelsov &lt;dorin@moorfinch.dk&gt;</b>, &nbsp;Ivo Marlek &lt;ivo@moorfinch.dk&gt;, &nbsp;&lt;lena@moorfinch.dk&gt;</p></li>
  </ul>
</main>
<footer class="abs site-footer">
  <div class="abs brand brand-foot"><span class="brand-dot"></span>Minutewell</div>
  <p class="abs copyright">© COPYRIGHT 2016. <b style="font-weight:600">MINUTEWELL</b></p>
  <ul class="abs foot-nav"><li class="active">HOME</li><li>PRIVACY</li><li>TERMS OF SERVICE</li></ul>
</footer>
</body>
</html>
```